Criação de Kit Layout de Posts para Redes Sociais (/suapagina, Instagram e etc) para Educação & Cursos
" Cursos Técnicos na área de saúde e Educação do Ensino fundamental ao Ensino Médio "

```html
<!DOCTYPE html>
<html lang="pt-BR">
<head>
<meta charset="utf-8">
<title>Curso de Radiologia Odontológica</title>
<link rel="stylesheet" href="https://fonts.googleapis.com/css2?family=Oswald:wght@500;600&family=Montserrat:wght@700;800&display=swap">
<style>
  :root {
    --navy: #0f2340;
    --deep: #1b3b63;
    --skin: #c99a86;
    --skin-light: #e3c2b3;
    --xray: #aab8c8;
    --brand-blue: #1f6fc6;
    --brand-blue-dark: #175aa6;
    --white: #ffffff;
    --ink: #1a2b45;
  }
  * { margin: 0; padding: 0; box-sizing: border-box; }
  html, body { width: 1200px; height: 1200px; overflow: hidden; background: var(--white); }
  .post {
    position: relative;
    width: 1200px;
    height: 1200px;
    overflow: hidden;
    font-family: "Montserrat", sans-serif;
  }
  .hero-photo {
    position: absolute;
    inset: 0 0 240px 0;
    background:
      radial-gradient(ellipse 380px 520px at 560px 560px, var(--skin-light) 0%, var(--skin) 45%, rgba(201,154,134,0) 80%),
      radial-gradient(ellipse 360px 560px at 930px 420px, var(--xray) 0%, rgba(170,184,200,0.5) 50%, rgba(170,184,200,0) 85%),
      linear-gradient(90deg, var(--navy) 0%, var(--deep) 30%, #5d6f86 60%, #8797ab 100%);
  }
  .base-shape {
    position: absolute;
    left: 0;
    bottom: 0;
    width: 1200px;
    height: 440px;
  }
  .headline {
    position: absolute;
    left: 96px;
    top: 358px;
    font-family: "Oswald", sans-serif;
    font-weight: 600;
    font-size: 74px;
    line-height: 82px;
    color: var(--white);
    letter-spacing: 0.5px;
  }
  .lead {
    position: absolute;
    left: 96px;
    top: 626px;
    width: 560px;
    font-weight: 800;
    font-size: 28px;
    line-height: 33px;
    color: var(--white);
    text-transform: uppercase;
  }
  .brand {
    position: absolute;
    left: 740px;
    top: 935px;
    display: flex;
    align-items: center;
    gap: 24px;
  }
  .brand-dot {
    width: 72px;
    height: 72px;
    border-radius: 50%;
    background: var(--white);
    flex: none;
  }
  .brand-name {
    font-family: "Oswald", sans-serif;
    font-weight: 600;
    font-size: 46px;
    line-height: 56px;
    color: var(--white);
    text-transform: uppercase;
    white-space: nowrap;
  }
  .contacts {
    position: absolute;
    left: 60px;
    top: 1036px;
    display: grid;
    grid-template-columns: 330px 300px;
    row-gap: 16px;
    font-weight: 700;
    font-size: 29px;
    color: var(--white);
  }
  .contact { display: flex; align-items: center; gap: 16px; height: 38px; }
  .contact-icon { width: 30px; height: 30px; flex: none; }
  .contact-dot { width: 24px; height: 24px; border-radius: 50%; border: 4px solid var(--white); flex: none; margin: 0 3px; }
</style>
</head>
<body>
<main class="post">
  <div class="hero-photo" role="img" aria-label="Rosto de mulher em close com metade sobreposta por imagem de raio-x do crânio, em tons de azul"></div>

  <svg class="base-shape" viewBox="0 0 1200 440" aria-hidden="true">
    <path d="M0 20 C 300 70, 700 40, 1200 0 L1200 440 L0 440 Z" fill="var(--white)"/>
    <path d="M0 110 C 320 160, 760 120, 1200 70 L1200 440 L0 440 Z" fill="var(--brand-blue)"/>
    <path d="M0 250 C 400 290, 800 260, 1200 220 L1200 440 L0 440 Z" fill="var(--brand-blue-dark)" opacity="0.35"/>
  </svg>

  <h1 class="headline">CURSO DE<br>RADIOLOGIA<br>ODONTOLOGICA</h1>

  <p class="lead">Oferecemos a melhor infraestrutura para seu futuro! Saiba mais sobre o curso, entre em contato!</p>

  <div class="brand">
    <span class="brand-dot"></span>
    <span class="brand-name">Vértice<br>Curso e Escola</span>
  </div>

  <div class="contacts">
    <div class="contact">
      <svg class="contact-icon" viewBox="0 0 24 24" aria-hidden="true"><path fill="var(--white)" d="M6.6 10.8a15.1 15.1 0 0 0 6.6 6.6l2.2-2.2c.3-.3.7-.4 1-.2 1.1.4 2.3.6 3.6.6.6 0 1 .4 1 1V20c0 .6-.4 1-1 1A17 17 0 0 1 3 4c0-.6.4-1 1-1h3.5c.6 0 1 .4 1 1 0 1.3.2 2.5.6 3.6.1.3 0 .7-.2 1z"/></svg>
      <span>(00) 0000-0000</span>
    </div>
    <div class="contact"><span class="contact-dot"></span><span>@seuperfil</span></div>
    <div class="contact">
      <svg class="contact-icon" viewBox="0 0 24 24" aria-hidden="true"><path fill="var(--white)" d="M6.6 10.8a15.1 15.1 0 0 0 6.6 6.6l2.2-2.2c.3-.3.7-.4 1-.2 1.1.4 2.3.6 3.6.6.6 0 1 .4 1 1V20c0 .6-.4 1-1 1A17 17 0 0 1 3 4c0-.6.4-1 1-1h3.5c.6 0 1 .4 1 1 0 1.3.2 2.5.6 3.6.1.3 0 .7-.2 1z"/></svg>
      <span>(00) 9 9999-9999</span>
    </div>
    <div class="contact"><span class="contact-dot"></span><span>/suapagina</span></div>
  </div>
</main>
</body>
</html>
```